Schema Paladin Powerpoint with Commander Ravelle Type Theme

Need powerpoint template with matching colors and different slide options. Logo and colors to be used can be found at schemapaladinhq.com. Want brightly colored slide deck that is readable form the back of a room, but highlights colors. I will be incorporating Trivano into the slides to gamify my presentations.

Target Market(s)

Tech

Industry/Entity Type

IT, specifically database, but crossing over to mental health in IT, important note this is not for a company, this is just for a professional building a brand

Font styles to use
Sans Serif

Colors
0054AA
0677BA
7BADD7
CADEEF
E8F1F8
EB3D1F
EC4F4E
F09395
F8D3D4
FCEDEE

Requirements
Must have
• My Logo in the bottom corner, front page, a thank your page, question page, content page, content page with two columns, content page with graphs, and icons to be used in the primary colors of the logos, About Me Page, Break Slides, Demo break slide
Should not have
• Lighter shades of colors, I want to pop out where colors are used, I want spacing and font size to be readable from the back of a room, most likely black text and white background

```html
<!DOCTYPE html>
<html lang="en">
<head>
<meta charset="utf-8">
<title>Schema Paladin – Slide Deck Overview</title>
<link href="https://fonts.googleapis.com/css2?family=Poppins:wght@300;400;500;600;700&display=swap" rel="stylesheet">
<style>
:root{
  --navy:#1c3f7d;
  --navy-deep:#17356c;
  --red:#e8222b;
  --gray:#8a8a8a;
  --ink:#333a45;
  --muted:#6b7280;
  --page:#e4e4e4;
  --white:#ffffff;
  --faint:#e6ecf6;
  --rule:#d9dde4;
}
*{box-sizing:border-box;margin:0;padding:0}
html,body{width:703px;height:1200px;overflow:hidden;background:var(--page)}
body{font-family:"Poppins",sans-serif;color:var(--ink)}
.deck{display:grid;grid-template-columns:repeat(3,227px);grid-auto-rows:127px;gap:5.5px 5px;padding:6px}
.slide{position:relative;background:var(--white);overflow:hidden}
.abs{position:absolute}
.brand{position:absolute;font-family:"Poppins",sans-serif;font-weight:700;letter-spacing:-.2px;white-space:nowrap;line-height:1}
.title{position:absolute;font-weight:600;color:var(--navy);line-height:1.05;white-space:nowrap}
.title.center{left:0;right:0;text-align:center}
.bar{position:absolute;height:2px;width:9px;background:var(--red)}
.body{position:absolute;font-size:2.6px;line-height:1.45;color:var(--muted);font-weight:400}
.rail{position:absolute;left:0;top:0;bottom:0;width:13px;background:var(--white);border-right:.5px solid #eef0f3}
.rail-mark{position:absolute;left:3px;top:3px;width:7px;height:7px;border-radius:50%;background:var(--navy);border:1.2px solid var(--red)}
.rail-name{position:absolute;left:6.5px;top:50%;transform:translate(-50%,-50%) rotate(-90deg);font-size:3.6px;font-weight:700;color:var(--red);white-space:nowrap}
.pg{position:absolute;left:5px;bottom:4px;font-size:2.6px;color:var(--ink)}
.photo{position:absolute}
.pill{position:absolute;border-radius:6px;background:var(--red);color:var(--white);font-size:3px;text-align:center;font-weight:500}
.card-text{font-size:2.5px;line-height:1.4;color:var(--white);text-align:center}
.lbl{position:absolute;font-size:3.2px;font-weight:600;color:var(--ink);white-space:nowrap}
.table{position:absolute;left:25px;top:30px;border-collapse:collapse;font-size:2.4px}
.table td,.table th{height:9.8px;text-align:center;border-bottom:.5px solid var(--rule)}
.table th{background:var(--red);color:var(--white);font-weight:500;width:35px}
.table td.rowhead{background:var(--navy);color:var(--white);width:55px;font-weight:500;border-bottom:.6px solid #fff}
.table td{color:var(--muted)}
.chev{position:absolute;top:45px;height:17px}
.qa{position:absolute;width:15px;height:15px;border-radius:2px;color:#fff;font-weight:600;font-size:7px;display:flex;align-items:center;justify-content:center}
.qa.q{background:var(--navy)}
.qa.a{background:var(--red)}
.contact{position:absolute;left:31px;width:61px;height:15px;background:#fff;box-shadow:0 0 3px rgba(0,0,0,.08);font-size:2.6px;color:var(--muted);display:flex;align-items:center;gap:5px;padding-left:5px}
.contact.lead{background:var(--navy);color:#fff}
</style>
</head>
<body>
<main class="deck">

<!-- 1 cover -->
<section class="slide">
  <div class="photo" role="img" aria-label="Photo of a presenter pointing at a screen, tinted navy" style="inset:0;background:linear-gradient(135deg,#284b8a,#1a3a74 60%,#21447f)"></div>
  <div class="brand" style="left:0;right:0;top:23px;text-align:center;font-size:8px;color:#fff">Schema Paladin</div>
  <div class="abs" style="left:84px;top:38px;width:60px;height:7px;border-radius:4px;background:rgba(255,255,255,.18);font-size:2.6px;color:#dfe6f3;text-align:center;line-height:7px;letter-spacing:.6px">www.schemapaladinhq.com</div>
  <div class="title center" style="top:51px;font-size:15px;color:#fff;font-weight:600">Presentation<br>Title Goes Here</div>
  <div class="abs" style="left:0;right:0;top:86px;text-align:center;font-size:5px;color:#e8edf6">Sub Title Goes Here</div>
  <div class="pill" style="left:86px;top:108px;width:48px;height:8px;line-height:8px">Oct 2021</div>
</section>

<!-- 2 title with footer -->
<section class="slide">
  <div class="photo" role="img" aria-label="Photo of hands at a desk, tinted navy" style="left:0;top:0;right:0;height:107px;background:linear-gradient(120deg,#244682,#1c3f7d 55%,#2a4d88)"></div>
  <div class="title" style="left:12px;top:41px;font-size:12px;color:#fff">TITLE OF<br>PRESENTATION</div>
  <div class="abs" style="left:13px;top:82px;font-size:3.2px;line-height:1.4;color:#dbe3f0">Here is A place for Credentials<br>Date: 2021 March</div>
  <div class="brand" style="left:10px;top:111px;font-size:8px;color:var(--red)">Schema Paladin</div>
  <div class="abs" style="right:17px;top:115px;font-size:3.2px;font-weight:600;color:var(--navy)">Presenter Name</div>
</section>

<!-- 3 title full navy -->
<section class="slide">
  <div class="photo" role="img" aria-label="Photo of server racks, tinted navy" style="inset:0;background:linear-gradient(90deg,#1c3f7d,#23498a 60%,#2f5796)"></div>
  <div class="brand" style="left:15px;top:35px;font-size:5px;color:var(--red)">Schema Paladin</div>
  <div class="title" style="left:14px;top:49px;font-size:12px;color:#fff">TITLE OF<br>PRESENTATION</div>
  <div class="abs" style="left:15px;top:90px;font-size:3.2px;line-height:1.4;color:#dbe3f0">Here is A place for Credentials<br>Date: 2021 March</div>
</section>

<!-- 4 angled title -->
<section class="slide" style="background:var(--navy)">
  <svg class="abs" style="inset:0" width="227" height="127" viewBox="0 0 227 127">
    <polygon points="138,0 227,0 227,127 108,127" fill="#c9ced6" role="img" aria-label="Photo of a laptop on a wooden desk"/>
    <polygon points="86,65 227,65 227,99 62,99" fill="var(--red)"/>
  </svg>
  <div class="brand" style="left:22px;top:30px;font-size:11px;color:#fff">Schema Paladin</div>
  <div class="title" style="left:99px;top:70px;font-size:11px;color:#fff;text-align:center;width:110px">Presentation<br>Title Goes Here</div>
</section>

<!-- 5 light title -->
<section class="slide">
  <div class="brand" style="left:153px;top:50px;font-size:14px;color:var(--faint);transform:rotate(-8deg)">Schema Paladin</div>
  <div class="brand" style="left:15px;top:28px;font-size:8px;color:var(--red)">Schema Paladin</div>
  <div class="title" style="left:14px;top:48px;font-size:14px">Presentation<br>Title Goes Here</div>
  <div class="abs" style="left:14px;top:77px;font-size:4.6px;color:var(--red)">Sub Title Goes Here</div>
  <div class="pill" style="left:12px;top:100px;width:68px;height:8px;line-height:8px;letter-spacing:.8px;font-size:2.8px">www.schemapaladinhq.com</div>
</section>

<!-- 6 about me -->
<section class="slide">
  <div class="rail"><div class="rail-mark"></div><div class="rail-name">Schema Paladin</div></div>
  <svg class="abs" style="left:20px;top:30px" width="60" height="60" viewBox="0 0 60 60">
    <g stroke="var(--navy)" stroke-width="2.2">
      <line x1="2" y1="24" x2="24" y2="2"/><line x1="2" y1="32" x2="30" y2="4"/><line x1="3" y1="40" x2="36" y2="7"/><line x1="6" y1="45" x2="40" y2="11"/>
    </g>
    <circle cx="34" cy="30" r="24" fill="#3b3b3b" role="img" aria-label="Portrait photo placeholder"/>
  </svg>
  <div class="abs" style="left:26px;top:93px;width:60px;text-align:center;font-size:4px;font-weight:600;color:var(--navy)">Name, Last Name</div>
  <div class="abs" style="left:26px;top:98px;width:60px;text-align:center;font-size:2.8px;color:var(--red);letter-spacing:1px">MANAGER</div>
  <div class="abs" style="left:90px;top:21px;bottom:14px;width:.5px;background:var(--rule)"></div>
  <div class="abs" style="left:99px;top:19px;font-size:5px;color:var(--red)">Manager</div>
  <div class="title" style="left:99px;top:25px;font-size:10px">Name, Last Name</div>
  <div class="body" style="left:99px;top:45px;width:118px;text-align:justify"><span style="color:var(--red)">Brief opening line about who you are.</span> Database specialist with a focus on clean schemas, steady performance and calm teams. I help engineers build systems that scale and stay easy to maintain over many years of growth and change.</div>
  <div class="body" style="left:99px;top:74px;width:118px;text-align:justify">Speaker and mentor on data design, query tuning and mental health in IT. Sessions mix practical demos with short quiz rounds so the room stays involved and every idea is easy to follow from the back row.</div>
</section>

<!-- 7 welcome -->
<section class="slide">
  <div class="rail"><div class="rail-mark"></div><div class="rail-name">Schema Paladin</div><div class="pg">7</div></div>
  <div class="photo" role="img" aria-label="Portrait photo placeholder" style="left:27px;top:31px;width:64px;height:64px;border-radius:6px;background:#2e2e2e"></div>
  <div class="abs" style="left:43px;top:87px;width:59px;height:10px;background:var(--red);color:#fff;font-size:5px;font-weight:600;line-height:10px;text-align:center;border-radius:0 0 2px 2px">Your Name</div>
  <div class="title" style="left:113px;top:20px;font-size:10px">Welcome Message</div>
  <div class="abs" style="left:113px;top:28px;font-size:16px;color:#c8ccd2">“</div>
  <div class="body" style="left:117px;top:42px;width:100px;text-align:center">Thank you for joining today. This talk covers how we design data, share knowledge and keep our teams healthy.</div>
  <div class="body" style="left:118px;top:63px;width:99px;text-align:justify">We will walk through real examples, short demos and a few quiz rounds. Ask questions at any point and share your own stories as we go. The aim is simple: leave with one idea you can use on Monday and one habit that protects your focus and energy at work.</div>
</section>

<!-- 8 slide break -->
<section class="slide">
  <div class="abs" style="left:0;right:0;top:0;height:5px;background:var(--navy)"></div>
  <div class="abs" style="left:0;right:0;bottom:0;height:5px;background:var(--red)"></div>
  <div class="abs" style="left:8px;top:24px;font-size:28px;font-weight:600;color:#dfe5ee">01</div>
  <div class="title" style="left:21px;top:40px;font-size:19px;font-weight:300;line-height:.95">Slide<br>Break</div>
  <div class="body" style="left:21px;top:77px;width:98px">A short pause before the next section. Take a breath, stretch, and get ready for the next quiz round on data design.</div>
  <div class="abs" style="left:151px;top:30px;width:46px;height:46px;border-radius:50%;background:var(--navy)"></div>
  <div class="brand" style="left:137px;top:82px;font-size:7px;color:var(--navy)">Schema Paladin</div>
</section>

<!-- 9 title and body -->
<section class="slide">
  <div class="rail"><div class="rail-mark"></div><div class="rail-name">Schema Paladin</div><div class="pg">9</div></div>
  <div class="title" style="left:20px;top:13px;font-size:10px">Title And Body Slide</div>
  <div class="bar" style="left:21px;top:25px"></div>
  <div class="brand" style="left:95px;top:55px;font-size:19px;color:var(--faint)">Schema Paladin</div>
</section>

<!-- 10 title and body text -->
<section class="slide">
  <div class="rail"><div class="rail-mark"></div><div class="rail-name">Schema Paladin</div></div>
  <div class="title" style="left:20px;top:13px;font-size:10px">Title And Body Slide</div>
  <div class="bar" style="left:21px;top:25px"></div>
  <div class="body" style="left:22px;top:39px;width:190px;text-align:justify">Body text goes here in a clear and simple paragraph. Keep each point short so it reads well from the back of the room, and let the key message stand out with one strong line at the start of each block.</div>
  <div class="body" style="left:22px;top:55px;width:190px;text-align:justify">Use this space for the main argument of the section. Describe the problem, the approach and the result. Add a short example that links the idea to daily database work so the audience can see how it applies to their own projects and teams.</div>
  <div class="body" style="left:22px;top:75px;width:190px;text-align:justify">Close with a summary and a question for the room. This is a good place for a quick poll or a quiz round before moving on. Keep timing tight and leave space for follow up questions, shared stories and short notes on healthy working habits in IT. Each paragraph should carry one idea only, so people can follow along, remember the point and act on it after the session ends.</div>
</section>

<!-- 11 pic and text -->
<section class="slide">
  <div class="rail"><div class="rail-mark"></div><div class="rail-name">Schema Paladin</div><div class="pg">11</div></div>
  <div class="title" style="left:22px;top:38px;font-size:12px">Pic And Text</div>
  <div class="bar" style="left:23px;top:52px"></div>
  <div class="body" style="left:22px;top:62px;width:78px;text-align:justify">Short text that explains the picture. Describe the setting, the task and why it matters. Keep lines brief so the message is clear at a glance and easy to read from far away in a large room.</div>
  <div class="abs" style="left:112px;top:16px;width:74px;height:70px;background:var(--red)"></div>
  <div class="photo" role="img" aria-label="Photo of a person typing on a keyboard at a desk" style="left:124px;top:29px;width:93px;height:81px;background:linear-gradient(135deg,#cfd3d8,#a7adb6);box-shadow:0 2px 5px rgba(0,0,0,.25)"></div>
</section>

<!-- 12 quote with photo -->
<section class="slide">
  <div class="photo" role="img" aria-label="Photo of a hiker on a mountain peak at dawn" style="left:0;top:0;width:98px;height:127px;background:linear-gradient(180deg,#4a5a6a,#2a333d)"></div>
  <div class="abs" style="left:112px;top:36px;width:24px;height:1.2px;background:var(--red)"></div>
  <div class="abs" style="left:112px;top:40px;width:100px;font-size:5.6px;font-weight:600;color:var(--navy);line-height:1.25">Success is not only what you achieve in your life, but also what you inspire in the lives of others</div>
  <div class="abs" style="left:52px;top:84px;right:0;bottom:0;background:var(--navy)"></div>
  <div class="abs" style="left:66px;top:96px;width:45px;font-size:3.2px;font-weight:600;color:#fff">Lorem ipsum dolor<div style="font-weight:400;font-size:2.3px;margin-top:3px;line-height:1.4">Short note about this point, kept clear</div></div>
  <div class="abs" style="left:120px;top:96px;width:45px;font-size:3.2px;font-weight:600;color:#fff">Lorem ipsum dolor<div style="font-weight:400;font-size:2.3px;margin-top:3px;line-height:1.4">Short note about this point, kept clear</div></div>
  <div class="abs" style="left:176px;top:96px;width:45px;font-size:3.2px;font-weight:600;color:#fff">Lorem ipsum dolor<div style="font-weight:400;font-size:2.3px;margin-top:3px;line-height:1.4">Short note about this point, kept clear</div></div>
</section>

<!-- 13 icons row -->
<section class="slide">
  <div class="rail"><div class="rail-mark"></div><div class="rail-name">Schema Paladin</div><div class="pg">13</div></div>
  <div class="abs" style="left:13px;top:0;right:0;height:60px;background:var(--navy)"></div>
  <div class="title center" style="left:13px;top:19px;font-size:10px;color:#fff">Here Add Awesome Text</div>
  <div class="bar" style="left:115px;top:32px"></div>
  <svg class="abs" style="left:0;top:0" width="227" height="127" viewBox="0 0 227 127">
    <g fill="var(--red)"><circle cx="60" cy="62" r="12"/><circle cx="122" cy="62" r="12"/><circle cx="185" cy="62" r="12"/></g>
    <g fill="none" stroke="#fff" stroke-width=".9">
      <circle cx="60" cy="62" r="5"/><circle cx="60" cy="62" r="2.5"/><line x1="60" y1="62" x2="66" y2="56"/>
      <path d="M118 66 l8 -8 m-3 0 h3 v3 M118 66 l-1 2 l2 -1"/>
      <rect x="180" y="60" width="2" height="5"/><rect x="184" y="57" width="2" height="8"/><rect x="188" y="55" width="2" height="10"/>
    </g>
  </svg>
  <div class="lbl" style="left:40px;top:79px;width:40px;text-align:center">Project name</div>
  <div class="lbl" style="left:102px;top:79px;width:40px;text-align:center">Project name</div>
  <div class="lbl" style="left:165px;top:79px;width:40px;text-align:center">Project name</div>
  <div class="body" style="left:32px;top:86px;width:56px;text-align:center">Short line of text that explains this project and its main result.</div>
  <div class="body" style="left:94px;top:86px;width:56px;text-align:center">Short line of text that explains this project and its main result.</div>
  <div class="body" style="left:157px;top:86px;width:56px;text-align:center">Short line of text that explains this project and its main result.</div>
</section>

<!-- 14 three columns -->
<section class="slide">
  <div class="rail"><div class="rail-mark"></div><div class="rail-name">Schema Paladin</div><div class="pg">14</div></div>
  <div class="title center" style="left:13px;top:14px;font-size:10px">3 Columns Slide</div>
  <div class="bar" style="left:115px;top:27px"></div>
  <div class="abs" style="left:31px;top:52px;width:52px;height:46px;background:var(--red);border-radius:2px"></div>
  <div class="abs" style="left:89px;top:52px;width:52px;height:46px;background:var(--navy);border-radius:2px"></div>
  <div class="abs" style="left:146px;top:52px;width:52px;height:46px;background:var(--gray);border-radius:2px"></div>
  <svg class="abs" style="left:0;top:0" width="227" height="127" viewBox="0 0 227 127">
    <g fill="#fff" stroke="#e7e9ee" stroke-width=".5"><circle cx="57" cy="52" r="9"/><circle cx="115" cy="52" r="9"/><circle cx="172" cy="52" r="9"/></g>
    <g fill="none" stroke-width=".8">
      <g stroke="var(--red)"><circle cx="57" cy="52" r="2.5"/><line x1="51" y1="52" x2="54" y2="52"/><line x1="60" y1="52" x2="63" y2="52"/><line x1="57" y1="46" x2="57" y2="49"/><line x1="57" y1="55" x2="57" y2="58"/></g>
      <g stroke="var(--navy)"><circle cx="115" cy="52" r="5"/><circle cx="115" cy="52" r="2.5"/></g>
      <g stroke="var(--gray)"><circle cx="172" cy="50" r="2"/><circle cx="168" cy="55" r="1.6"/><circle cx="176" cy="55" r="1.6"/></g>
    </g>
  </svg>
  <div class="abs card-text" style="left:33px;top:66px;width:48px"><b style="font-weight:600;font-size:2.8px">Project name here</b><br>Short line of text that explains the idea and its value to the team.</div>
  <div class="abs card-text" style="left:91px;top:66px;width:48px"><b style="font-weight:600;font-size:2.8px">Project name here</b><br>Short line of text that explains the idea and its value to the team.</div>
  <div class="abs card-text" style="left:148px;top:66px;width:48px"><b style="font-weight:600;font-size:2.8px">Project name here</b><br>Short line of text that explains the idea and its value to the team.</div>
</section>

<!-- 15 screenshot -->
<section class="slide">
  <div class="rail"><div class="rail-mark"></div><div class="rail-name">Schema Paladin</div><div class="pg">15</div></div>
  <svg class="abs" style="left:0;top:0" width="227" height="127" viewBox="0 0 227 127">
    <polygon points="13,0 106,0 170,127 13,127" fill="var(--navy)"/>
    <rect x="102" y="27" width="120" height="82" rx="3" fill="#1f1f1f"/>
    <rect x="106" y="31" width="112" height="74" fill="#9b9b9b"/>
    <rect x="89" y="109" width="138" height="3" rx="1" fill="#cfd2d6"/>
  </svg>
  <div class="abs" style="left:106px;top:65px;width:112px;text-align:center;font-size:4px;font-weight:600;color:#fff">HERE YOU CAN ADD A SCREENSHOT</div>
  <div class="title" style="left:25px;top:40px;font-size:10px;color:#fff">A Place for<br>Screenshot</div>
  <div class="bar" style="left:26px;top:64px"></div>
  <div class="body" style="left:25px;top:72px;width:72px;color:#dbe3f0">Short text that explains what the screenshot shows and why it matters here.</div>
</section>

<!-- 16 six columns -->
<section class="slide">
  <div class="rail"><div class="rail-mark"></div><div class="rail-name">Schema Paladin</div><div class="pg">16</div></div>
  <div class="title center" style="left:13px;top:11px;font-size:10px">6 Columns Slide</div>
  <div class="bar" style="left:115px;top:24px"></div>
  <svg class="abs" style="left:0;top:0" width="227" height="127" viewBox="0 0 227 127">
    <g fill="#fff" stroke="#eceef2" stroke-width=".6">
      <circle cx="36" cy="47" r="6"/><circle cx="36" cy="71" r="6"/><circle cx="36" cy="95" r="6"/>
      <circle cx="134" cy="47" r="6"/><circle cx="134" cy="71" r="6"/><circle cx="134" cy="95" r="6"/>
    </g>
    <g fill="none" stroke="var(--navy)" stroke-width=".6">
      <rect x="33" y="44" width="6" height="7"/><rect x="131" y="44" width="6" height="7"/>
      <path d="M33 74 v-2 M35 74 v-3 M37 74 v-4 M39 74 v-5"/><path d="M131 74 v-2 M133 74 v-3 M135 74 v-4 M137 74 v-5"/>
      <circle cx="36" cy="94" r="2"/><circle cx="134" cy="94" r="2"/>
    </g>
  </svg>
  <div class="lbl" style="left:47px;top:42px;font-size:2.8px">Project name</div>
  <div class="body" style="left:47px;top:46px;width:62px">Short text about this project and what it delivers.</div>
  <div class="lbl" style="left:47px;top:66px;font-size:2.8px">Project name</div>
  <div class="body" style="left:47px;top:70px;width:62px">Short text about this project and what it delivers.</div>
  <div class="lbl" style="left:47px;top:90px;font-size:2.8px">Project name</div>
  <div class="body" style="left:47px;top:94px;width:62px">Short text about this project and what it delivers.</div>
  <div class="lbl" style="left:145px;top:42px;font-size:2.8px">Project name</div>
  <div class="body" style="left:145px;top:46px;width:62px">Short text about this project and what it delivers.</div>
  <div class="lbl" style="left:145px;top:66px;font-size:2.8px">Project name</div>
  <div class="body" style="left:145px;top:70px;width:62px">Short text about this project and what it delivers.</div>
  <div class="lbl" style="left:145px;top:90px;font-size:2.8px">Project name</div>
  <div class="body" style="left:145px;top:94px;width:62px">Short text about this project and what it delivers.</div>
</section>

<!-- 17 chart table -->
<section class="slide">
  <div class="rail"><div class="rail-mark"></div><div class="rail-name">Schema Paladin</div><div class="pg">17</div></div>
  <div class="title center" style="left:13px;top:10px;font-size:10px">Chart Slide</div>
  <div class="bar" style="left:115px;top:23px"></div>
  <table class="table">
    <tr><th style="background:transparent;width:55px"></th><th>Your Text Here</th><th>Your Text Here</th><th>Your Text Here</th><th>Your Text Here</th></tr>
    <tr><td class="rowhead">You can replace this text</td><td>1250</td><td style="color:var(--navy);font-size:5px">✔</td><td>50%</td><td>1250</td></tr>
    <tr><td class="rowhead">You can replace this text</td><td>3623</td><td style="color:var(--navy);font-size:5px">✖</td><td>50%</td><td>3623</td></tr>
    <tr><td class="rowhead">You can replace this text</td><td>2569</td><td style="color:var(--navy);font-size:5px">✔</td><td>12%</td><td>2569</td></tr>
    <tr><td class="rowhead">You can replace this text</td><td>1020</td><td style="color:var(--navy);font-size:5px">✖</td><td>65%</td><td>1020</td></tr>
    <tr><td class="rowhead">You can replace this text</td><td>2320</td><td style="color:var(--navy);font-size:5px">✔</td><td>36%</td><td>2320</td></tr>
    <tr><td class="rowhead">You can replace this text</td><td>5698</td><td style="color:var(--navy);font-size:5px">✖</td><td>95%</td><td>5698</td></tr>
    <tr><td class="rowhead">You can replace this text</td><td>1999</td><td style="color:var(--navy);font-size:5px">✖</td><td>66%</td><td>1999</td></tr>
  </table>
</section>

<!-- 18 smart art -->
<section class="slide">
  <div class="rail"><div class="rail-mark"></div><div class="rail-name">Schema Paladin</div><div class="pg">18</div></div>
  <div class="title" style="left:20px;top:12px;font-size:10px">Smart Art Slide</div>
  <div class="bar" style="left:21px;top:24px"></div>
  <svg class="abs" style="left:0;top:0" width="227" height="127" viewBox="0 0 227 127">
    <g fill="none" stroke="var(--navy)" stroke-width=".7">
      <circle cx="26" cy="51" r="3"/><circle cx="26" cy="51" r="1.3"/>
      <path d="M23 79 v-2 M25 79 v-3 M27 79 v-4 M29 79 v-5"/>
      <rect x="23" y="101" width="5" height="6"/>
    </g>
    <polygon points="167,31 191,70 177,83 157,83 143,70" fill="var(--navy)"/>
    <polygon points="141,74 154,88 185,88 191,74 197,116 119,116" fill="none"/>
    <polygon points="141,75 155,88 170,88 169,116 118,116" fill="var(--red)"/>
    <polygon points="193,75 217,116 173,116 173,88 180,88" fill="var(--gray)"/>
  </svg>
  <div class="abs card-text" style="left:150px;top:50px;width:34px"><b style="font-size:2.8px;font-weight:600">Project<br>name</b><br>Short note on this item</div>
  <div class="abs card-text" style="left:121px;top:93px;width:46px"><b style="font-size:2.8px;font-weight:600">Project name</b><br>Short note on this item</div>
  <div class="abs card-text" style="left:175px;top:93px;width:40px"><b style="font-size:2.8px;font-weight:600">Project name</b><br>Short note on this item</div>
  <div class="lbl" style="left:35px;top:45px;font-size:3px;color:var(--navy)">Lorem ipsum dolor</div>
  <div class="body" style="left:35px;top:49px;width:72px">Short line explaining this step in the process.</div>
  <div class="lbl" style="left:35px;top:71px;font-size:3px;color:var(--navy)">Lorem ipsum dolor</div>
  <div class="body" style="left:35px;top:75px;width:72px">Short line explaining this step in the process.</div>
  <div class="lbl" style="left:35px;top:97px;font-size:3px;color:var(--navy)">Lorem ipsum dolor</div>
  <div class="body" style="left:35px;top:101px;width:72px">Short line explaining this step in the process.</div>
</section>

<!-- 19 quotes -->
<section class="slide">
  <div class="rail"><div class="rail-mark"></div><div class="rail-name">Schema Paladin</div><div class="pg">19</div></div>
  <div class="title center" style="left:13px;top:10px;font-size:10px">Here is Quotes</div>
  <div class="bar" style="left:115px;top:23px"></div>
  <div class="abs" style="left:22px;top:32px;font-size:18px;font-weight:700;color:var(--red)">”</div>
  <div class="abs" style="left:127px;top:32px;font-size:18px;font-weight:700;color:var(--navy)">”</div>
  <div class="abs" style="left:22px;top:53px;width:80px;font-size:3.6px;line-height:1.5;color:var(--ink)">A short quote goes here about learning, data and growth. Keep it simple so it lands with the whole room and is easy to remember.</div>
  <div class="abs" style="left:127px;top:53px;width:80px;font-size:3.6px;line-height:1.5;color:var(--ink)">A short quote goes here about learning, data and growth. Keep it simple so it lands with the whole room and is easy to remember.</div>
  <div class="abs" style="left:22px;top:94px;width:11px;height:11px;border-radius:50%;background:#e3e5ea"></div>
  <div class="abs" style="left:37px;top:95px;font-size:3.2px;font-weight:600;color:var(--navy)">Your Name<div style="font-weight:400;color:var(--muted);font-size:2.8px">Founder</div></div>
  <div class="abs" style="left:127px;top:94px;width:11px;height:11px;border-radius:50%;background:#e3e5ea"></div>
  <div class="abs" style="left:142px;top:95px;font-size:3.2px;font-weight:600;color:var(--navy)">Your Name<div style="font-weight:400;color:var(--muted);font-size:2.8px">Founder</div></div>
</section>

<!-- 20 statistics circles -->
<section class="slide">
  <div class="rail"><div class="rail-mark"></div><div class="rail-name">Schema Paladin</div><div class="pg">20</div></div>
  <div class="title center" style="left:13px;top:12px;font-size:10px">Here Is Statistics</div>
  <div class="bar" style="left:115px;top:25px"></div>
  <svg class="abs" style="left:0;top:0" width="227" height="127" viewBox="0 0 227 127">
    <circle cx="52" cy="78" r="33" fill="var(--navy)"/>
    <circle cx="52" cy="91" r="20" fill="var(--red)"/>
    <circle cx="52" cy="99" r="12" fill="#555"/>
    <g stroke="#8a8f99" stroke-width=".4"><line x1="62" y1="53" x2="95" y2="53"/><line x1="72" y1="73" x2="95" y2="73"/><line x1="64" y1="97" x2="95" y2="97"/></g>
    <g fill="#fff" font-family="Poppins,sans-serif" font-size="8" font-weight="600" text-anchor="middle">
      <text x="52" y="59">$</text><text x="52" y="79">$</text><text x="52" y="103">$</text>
    </g>
    <g fill="var(--navy)" font-family="Poppins,sans-serif" font-size="6" font-weight="600">
      <text x="96" y="55">5M</text><text x="96" y="75">2M</text><text x="96" y="99">1M</text>
    </g>
    <rect x="130" y="52" width="8" height="8" fill="var(--navy)"/>
    <rect x="130" y="72" width="8" height="8" fill="var(--red)"/>
    <rect x="130" y="92" width="8" height="8" fill="#555"/>
    <g fill="none" stroke="#fff" stroke-width="1"><path d="M132 56 l1.5 1.5 l3 -3"/><path d="M132 76 l1.5 1.5 l3 -3"/><path d="M132 96 l1.5 1.5 l3 -3"/></g>
  </svg>
  <div class="lbl" style="left:142px;top:50px;font-size:3.2px;color:var(--navy)">Lorem ipsum dolor</div>
  <div class="body" style="left:142px;top:55px;width:70px">Short line about this figure and its trend.</div>
  <div class="lbl" style="left:142px;top:70px;font-size:3.2px;color:var(--navy)">Lorem ipsum dolor</div>
  <div class="body" style="left:142px;top:75px;width:70px">Short line about this figure and its trend.</div>
  <div class="lbl" style="left:142px;top:90px;font-size:3.2px;color:var(--navy)">Lorem ipsum dolor</div>
  <div class="body" style="left:142px;top:95px;width:70px">Short line about this figure and its trend.</div>
</section>

<!-- 21 progress rings -->
<section class="slide">
  <div class="rail"><div class="rail-mark"></div><div class="rail-name">Schema Paladin</div></div>
  <div class="title center" style="left:13px;top:12px;font-size:10px">Here Add Your Title</div>
  <div class="bar" style="left:115px;top:25px"></div>
  <div class="body" style="left:45px;top:35px;width:140px;text-align:center">Short intro text for this slide. Explain what the numbers below mean and why they matter to the audience in two clear lines.</div>
  <svg class="abs" style="left:0;top:0" width="227" height="127" viewBox="0 0 227 127">
    <g fill="none" stroke-width="2">
      <circle cx="64" cy="77" r="15" stroke="#eceef2"/><circle cx="64" cy="77" r="15" stroke="var(--red)" stroke-dasharray="47 94.2" transform="rotate(-90 64 77)"/>
      <circle cx="112" cy="77" r="15" stroke="#eceef2"/><circle cx="112" cy="77" r="15" stroke="var(--red)" stroke-dasharray="70.7 94.2" transform="rotate(-90 112 77)"/>
      <circle cx="160" cy="77" r="15" stroke="#eceef2"/><circle cx="160" cy="77" r="15" stroke="var(--red)" stroke-dasharray="37.7 94.2" transform="rotate(-90 160 77)"/>
    </g>
    <g fill="var(--navy)" font-family="Poppins,sans-serif" font-size="7" font-weight="600" text-anchor="middle">
      <text x="64" y="80">50%</text><text x="112" y="80">75%</text><text x="160" y="80">40%</text>
    </g>
  </svg>
  <div class="body" style="left:46px;top:98px;width:36px;text-align:center">Short label for this value</div>
  <div class="body" style="left:94px;top:98px;width:36px;text-align:center">Short label for this value</div>
  <div class="body" style="left:142px;top:98px;width:36px;text-align:center">Short label for this value</div>
</section>

<!-- 22 statistics line chart -->
<section class="slide">
  <div class="rail"><div class="rail-mark"></div><div class="rail-name">Schema Paladin</div><div class="pg">22</div></div>
  <div class="title center" style="left:13px;top:10px;font-size:10px;left:0;width:227px">Here is Statistics</div>
  <div class="bar" style="left:115px;top:23px"></div>
  <div class="abs" style="left:17px;top:38px;width:55px;height:32px;background:var(--navy);color:#fff;text-align:center;padding-top:6px;font-size:9px;font-weight:300">$0.5M<div style="font-size:2.8px">Revenue</div></div>
  <div class="abs" style="left:17px;top:72px;width:55px;height:32px;background:#fff;box-shadow:0 0 3px rgba(0,0,0,.1);color:var(--red);text-align:center;padding-top:6px;font-size:9px;font-weight:300">-0.28%<div style="font-size:2.8px">Revenue</div></div>
  <svg class="abs" style="left:0;top:0" width="227" height="127" viewBox="0 0 227 127">
    <g fill="#777" font-family="Poppins,sans-serif" font-size="2.2" text-anchor="end">
      <text x="97" y="32">$350,000</text><text x="97" y="41">$300,000</text><text x="97" y="49">$250,000</text><text x="97" y="58">$200,000</text><text x="97" y="66">$150,000</text><text x="97" y="75">$100,000</text><text x="97" y="83">$50,000</text><text x="97" y="92">$-</text>
    </g>
    <g fill="#777" font-family="Poppins,sans-serif" font-size="2.2" text-anchor="middle">
      <text x="104" y="97">Jan</text><text x="114" y="97">Feb</text><text x="123" y="97">Mar</text><text x="133" y="97">Apr</text><text x="142" y="97">May</text><text x="152" y="97">Jun</text><text x="161" y="97">Jul</text><text x="171" y="97">Aug</text><text x="180" y="97">Sep</text><text x="190" y="97">Oct</text><text x="199" y="97">Nov</text><text x="209" y="97">Dec</text><text x="218" y="97">Jan</text>
    </g>
    <path d="M125 91 C132 88 134 72 140 66 C146 60 150 68 154 64 C158 58 166 58 172 64 C178 70 182 62 186 64 C190 68 192 74 196 64 C200 52 204 50 208 58 C212 62 214 40 220 38" fill="none" stroke="var(--red)" stroke-width=".6"/>
  </svg>
</section>

<!-- 23 timeline -->
<section class="slide">
  <div class="rail"><div class="rail-mark"></div><div class="rail-name">Schema Paladin</div><div class="pg">23</div></div>
  <div class="title center" style="left:13px;top:13px;font-size:10px">Company Timeline</div>
  <div class="bar" style="left:115px;top:26px"></div>
  <svg class="abs" style="left:0;top:0" width="227" height="127" viewBox="0 0 227 127">
    <g>
      <polygon points="21,45 56,45 62,53.5 56,62 21,62 27,53.5" fill="var(--red)"/>
      <polygon points="58,45 93,45 99,53.5 93,62 58,62 64,53.5" fill="var(--navy)"/>
      <polygon points="95,45 130,45 136,53.5 130,62 95,62 101,53.5" fill="var(--red)"/>
      <polygon points="132,45 167,45 173,53.5 167,62 132,62 138,53.5" fill="var(--navy)"/>
      <polygon points="169,45 204,45 210,53.5 204,62 169,62 175,53.5" fill="var(--red)"/>
    </g>
    <g fill="#fff" font-family="Poppins,sans-serif" font-size="4.2" font-weight="600" text-anchor="middle">
      <text x="41" y="55">STEP 01</text><text x="78" y="55">STEP 02</text><text x="115" y="55">STEP 03</text><text x="152" y="55">STEP 04</text><text x="189" y="55">STEP 05</text>
    </g>
    <line x1="21" y1="68" x2="210" y2="68" stroke="#cfd3da" stroke-width=".5"/>
    <g stroke="#cfd3da" stroke-width=".4" fill="#fff">
      <line x1="42" y1="68" x2="42" y2="76"/><line x1="79" y1="68" x2="79" y2="76"/><line x1="116" y1="68" x2="116" y2="76"/><line x1="153" y1="68" x2="153" y2="76"/><line x1="190" y1="68" x2="190" y2="76"/>
      <circle cx="42" cy="76" r="1"/><circle cx="79" cy="76" r="1"/><circle cx="116" cy="76" r="1"/><circle cx="153" cy="76" r="1"/><circle cx="190" cy="76" r="1"/>
    </g>
  </svg>
  <div class="lbl" style="left:24px;top:82px;width:36px;text-align:center">Project name</div>
  <div class="lbl" style="left:61px;top:82px;width:36px;text-align:center">Project name</div>
  <div class="lbl" style="left:98px;top:82px;width:36px;text-align:center">Project name</div>
  <div class="lbl" style="left:135px;top:82px;width:36px;text-align:center">Project name</div>
  <div class="lbl" style="left:172px;top:82px;width:36px;text-align:center">Project name</div>
  <div class="body" style="left:26px;top:89px;width:32px;text-align:center">Short note on this milestone and date.</div>
  <div class="body" style="left:63px;top:89px;width:32px;text-align:center">Short note on this milestone and date.</div>
  <div class="body" style="left:100px;top:89px;width:32px;text-align:center">Short note on this milestone and date.</div>
  <div class="body" style="left:137px;top:89px;width:32px;text-align:center">Short note on this milestone and date.</div>
  <div class="body" style="left:174px;top:89px;width:32px;text-align:center">Short note on this milestone and date.</div>
</section>

<!-- 24 Q&A -->
<section class="slide">
  <div class="rail"><div class="rail-mark"></div><div class="rail-name">Schema Paladin</div><div class="pg">24</div></div>
  <div class="title center" style="left:13px;top:13px;font-size:10px">Q&amp;A Slide</div>
  <div class="bar" style="left:115px;top:26px"></div>
  <div class="qa q" style="left:30px;top:35px">Q</div><div class="body" style="left:49px;top:36px;width:55px">A short question from the audience goes here in two lines.</div>
  <div class="qa q" style="left:30px;top:53px">Q</div><div class="body" style="left:49px;top:54px;width:55px">A short question from the audience goes here in two lines.</div>
  <div class="qa q" style="left:30px;top:72px">Q</div><div class="body" style="left:49px;top:73px;width:55px">A short question from the audience goes here in two lines.</div>
  <div class="qa q" style="left:30px;top:91px">Q</div><div class="body" style="left:49px;top:92px;width:55px">A short question from the audience goes here in two lines.</div>
  <div class="qa a" style="left:130px;top:35px">A</div><div class="body" style="left:149px;top:36px;width:55px">A short answer that responds to the question above.</div>
  <div class="qa a" style="left:130px;top:53px">A</div><div class="body" style="left:149px;top:54px;width:55px">A short answer that responds to the question above.</div>
  <div class="qa a" style="left:130px;top:72px">A</div><div class="body" style="left:149px;top:73px;width:55px">A short answer that responds to the question above.</div>
  <div class="qa a" style="left:130px;top:91px">A</div><div class="body" style="left:149px;top:92px;width:55px">A short answer that responds to the question above.</div>
</section>

<!-- 25 thank you -->
<section class="slide" style="background:linear-gradient(135deg,#f4f5f7,#eceef1)">
  <div class="brand" style="left:33px;top:15px;font-size:8px;color:var(--red)">Schema Paladin</div>
  <div class="contact lead" style="top:33px">
    <svg width="5" height="5" viewBox="0 0 10 10"><circle cx="5" cy="5" r="4" fill="none" stroke="#fff"/><line x1="1" y1="5" x2="9" y2="5" stroke="#fff"/></svg>www.schemapaladinhq.com</div>
  <div class="contact" style="top:50px">
    <svg width="5" height="6" viewBox="0 0 10 12"><path d="M5 11 C1 6 1 5 1 4 a4 4 0 0 1 8 0 c0 1 0 2 -4 7z" fill="var(--navy)"/></svg>Write your<br>studio address</div>
  <div class="contact" style="top:67px">
    <svg width="5" height="5" viewBox="0 0 10 10"><path d="M2 1 l2 0 l1 3 l-1.5 1 a6 6 0 0 0 2.5 2.5 l1 -1.5 l3 1 l0 2 c-5 0 -8 -3 -8 -8z" fill="var(--navy)"/></svg>(555) 014-2290</div>
  <div class="contact" style="top:84px">
    <svg width="5" height="4" viewBox="0 0 10 8"><rect width="10" height="8" fill="var(--navy)"/><path d="M0 0 l5 4 l5 -4" fill="none" stroke="#fff" stroke-width=".8"/></svg>info@schemapaladinhq.com</div>
  <div class="abs" style="left:52px;top:105px;display:flex;gap:2px">
    <span style="width:4px;height:4px;background:var(--navy);border-radius:1px"></span><span style="width:4px;height:4px;background:var(--navy);border-radius:1px"></span><span style="width:4px;height:4px;background:var(--navy);border-radius:1px"></span><span style="width:4px;height:4px;background:var(--navy);border-radius:1px"></span>
  </div>
  <div class="title" style="left:125px;top:58px;font-size:14px;font-weight:600">THANK YOU</div>
</section>

<!-- 26 questions -->
<section class="slide">
  <div class="rail"><div class="rail-mark"></div><div class="rail-name">Schema Paladin</div><div class="pg">26</div></div>
  <svg class="abs" style="left:0;top:0" width="227" height="127" viewBox="0 0 227 127">
    <path d="M55 26 L183 19 L180 93 L92 97 L78 114 L82 98 L60 99 Z" fill="none" stroke="var(--navy)" stroke-width=".8"/>
    <path d="M58 24 L186 22 L177 96 L95 100 L74 111 L79 101 L63 102 Z" fill="none" stroke="var(--red)" stroke-width=".8"/>
    <path d="M61 30 L176 28 L173 90 L95 93 L81 106 L84 93 L64 94 Z" fill="#fff" style="filter:drop-shadow(0 1px 2px rgba(0,0,0,.2))"/>
  </svg>
  <div class="title" style="left:60px;top:54px;width:115px;text-align:center;font-size:12px">Questions?</div>
</section>

</main>
</body>
</html>
```